we are a college and require a design of a printable graduation certificate

our courses range from certicate III to Diploma

We would a high quality design, similar to a unveristy degree, so its meaning full to the students and looks great on the wall

our college website is: www.marlowinstitute.example.au

Industry/Entity Type

College

Requirements
Must have
• security feature like water mark or stamp

```html
<!DOCTYPE html>
<html lang="en">
<head>
<meta charset="utf-8">
<title>Marlow Institute – Certificate of Graduation</title>
<link rel="stylesheet" href="https://fonts.googleapis.com/css2?family=Pirata+One&family=Uncial+Antiqua&display=swap">
<style>
  :root {
    --paper: #ece8dc;
    --ink: #3b6a74;
    --ink-deep: #2f5a63;
    --band: #4f7f89;
    --band-dark: #3f6e78;
    --band-light: #8fb0b6;
    --seal: #8fa6ab;
  }
  * { margin: 0; padding: 0; box-sizing: border-box; }
  html, body { width: 1200px; height: 886px; overflow: hidden; background: var(--paper); }
  .certificate { position: relative; width: 1200px; height: 886px; background: var(--paper); color: var(--ink); }
  .frame { position: absolute; inset: 0; }
  .college-name {
    position: absolute; top: 192px; left: 0; width: 1200px; text-align: center;
    font-family: "Uncial Antiqua", serif; font-size: 15px; font-weight: 400; color: var(--ink-deep); letter-spacing: 0.5px;
  }
  .title {
    position: absolute; top: 228px; left: 0; width: 1200px; text-align: center;
    font-family: "Pirata One", serif; font-weight: 400; font-size: 86px; line-height: 1; color: var(--ink-deep); letter-spacing: 1.5px;
  }
  .body-text {
    position: absolute; left: 0; width: 1200px; text-align: center;
    font-family: "Uncial Antiqua", serif; font-size: 17px; line-height: 1; color: var(--ink-deep); letter-spacing: 0.6px;
  }
  .fill-line { position: absolute; height: 0; border-top: 2px dotted var(--ink); }
  .signature-label {
    position: absolute; width: 200px; text-align: center;
    font-family: "Uncial Antiqua", serif; font-size: 13px; color: var(--ink-deep);
  }
</style>
</head>
<body>
<main class="certificate">
  <svg class="frame" width="1200" height="886" viewBox="0 0 1200 886">
    <defs>
      <radialGradient id="medallion-fill" cx="50%" cy="50%" r="50%">
        <stop offset="0" stop-color="#dfe6e3"/>
        <stop offset="0.45" stop-color="var(--band-light)"/>
        <stop offset="1" stop-color="var(--band)"/>
      </radialGradient>
      <radialGradient id="seal-fill" cx="50%" cy="50%" r="50%">
        <stop offset="0.18" stop-color="var(--paper)"/>
        <stop offset="0.3" stop-color="#a9bcbf"/>
        <stop offset="0.75" stop-color="var(--seal)"/>
        <stop offset="1" stop-color="var(--paper)" stop-opacity="0.2"/>
      </radialGradient>
      <radialGradient id="watermark-fill" cx="50%" cy="50%" r="50%">
        <stop offset="0" stop-color="#3b6a74" stop-opacity="0.07"/>
        <stop offset="1" stop-color="#3b6a74" stop-opacity="0"/>
      </radialGradient>
      <linearGradient id="band-h" x1="0" y1="0" x2="0" y2="1">
        <stop offset="0" stop-color="var(--band-dark)"/>
        <stop offset="0.5" stop-color="#6a959e"/>
        <stop offset="1" stop-color="var(--band-dark)"/>
      </linearGradient>
      <linearGradient id="band-v" x1="0" y1="0" x2="1" y2="0">
        <stop offset="0" stop-color="var(--band-dark)"/>
        <stop offset="0.5" stop-color="#6a959e"/>
        <stop offset="1" stop-color="var(--band-dark)"/>
      </linearGradient>
    </defs>

    <!-- faint security watermark field -->
    <ellipse class="watermark" cx="606" cy="520" rx="420" ry="220" fill="url(#watermark-fill)" role="img" aria-label="Faint security watermark"/>

    <!-- border bands -->
    <g class="border-bands" role="img" aria-label="Guilloche patterned border bands">
      <rect x="63" y="57" width="1077" height="44" fill="url(#band-h)"/>
      <rect x="63" y="784" width="1077" height="44" fill="url(#band-h)"/>
      <rect x="84" y="57" width="44" height="771" fill="url(#band-v)"/>
      <rect x="1073" y="57" width="44" height="771" fill="url(#band-v)"/>
      <g fill="none" stroke="var(--band-light)" stroke-width="0.8" opacity="0.7">
        <rect x="91" y="64" width="1019" height="757"/>
        <rect x="121" y="94" width="959" height="697"/>
      </g>
    </g>

    <!-- thin rule frames -->
    <g fill="none" stroke="var(--ink)">
      <rect x="76" y="49" width="1048" height="788" stroke-width="1.2"/>
      <rect x="136" y="109" width="929" height="667" stroke-width="1.5"/>
      <rect x="142" y="115" width="917" height="655" stroke-width="0.8"/>
    </g>

    <!-- top centre opening for institute name -->
    <rect x="512" y="40" width="188" height="70" fill="var(--paper)"/>
    <circle cx="606" cy="150" r="24" fill="none" stroke="var(--ink)" stroke-width="2"/>

    <!-- corner medallions -->
    <g class="corner-medallions" role="img" aria-label="Ornamental corner rosettes">
      <g transform="translate(97 80)">
        <circle r="62" fill="var(--paper)" stroke="var(--ink)" stroke-width="2"/>
        <circle r="55" fill="url(#medallion-fill)"/>
        <circle r="42" fill="none" stroke="var(--paper)" stroke-width="1"/>
        <circle r="28" fill="none" stroke="var(--ink)" stroke-width="1"/>
        <circle r="5" fill="var(--ink-deep)"/>
      </g>
      <g transform="translate(1103 80)">
        <circle r="62" fill="var(--paper)" stroke="var(--ink)" stroke-width="2"/>
        <circle r="55" fill="url(#medallion-fill)"/>
        <circle r="42" fill="none" stroke="var(--paper)" stroke-width="1"/>
        <circle r="28" fill="none" stroke="var(--ink)" stroke-width="1"/>
        <circle r="5" fill="var(--ink-deep)"/>
      </g>
      <g transform="translate(97 806)">
        <circle r="62" fill="var(--paper)" stroke="var(--ink)" stroke-width="2"/>
        <circle r="55" fill="url(#medallion-fill)"/>
        <circle r="42" fill="none" stroke="var(--paper)" stroke-width="1"/>
        <circle r="28" fill="none" stroke="var(--ink)" stroke-width="1"/>
        <circle r="5" fill="var(--ink-deep)"/>
      </g>
      <g transform="translate(1103 806)">
        <circle r="62" fill="var(--paper)" stroke="var(--ink)" stroke-width="2"/>
        <circle r="55" fill="url(#medallion-fill)"/>
        <circle r="42" fill="none" stroke="var(--paper)" stroke-width="1"/>
        <circle r="28" fill="none" stroke="var(--ink)" stroke-width="1"/>
        <circle r="5" fill="var(--ink-deep)"/>
      </g>
    </g>

    <!-- security seal -->
    <g class="security-seal" transform="translate(604 694)" role="img" aria-label="Guilloche security seal rosette">
      <circle r="68" fill="url(#seal-fill)"/>
      <circle r="50" fill="none" stroke="var(--paper)" stroke-width="0.8" opacity="0.8"/>
      <circle r="34" fill="none" stroke="var(--paper)" stroke-width="0.8" opacity="0.8"/>
    </g>

    <!-- signature lines -->
    <line x1="313" y1="700" x2="460" y2="700" stroke="var(--ink)" stroke-width="1"/>
    <line x1="743" y1="700" x2="887" y2="700" stroke="var(--ink)" stroke-width="1"/>
  </svg>

  <div class="college-name">MARLOW INSTITUTE</div>

  <h1 class="title">Certificate of Graduation</h1>

  <p class="body-text" style="top:342px">Be it known that</p>
  <div class="fill-line" style="left:440px; top:412px; width:343px"></div>
  <p class="body-text" style="top:424px">having completed the studies and satisfied the requirements</p>
  <p class="body-text" style="top:450px">for the degree of</p>
  <div class="fill-line" style="left:440px; top:514px; width:343px"></div>
  <p class="body-text" style="top:526px">has accordingly been admited to that degree with all Rights and</p>
  <p class="body-text" style="top:551px">Privileges thereunto appertaining.</p>
  <p class="body-text" style="top:576px">In Withness Whereof, we have caused this diploma to be signed and our seal</p>
  <p class="body-text" style="top:603px">to be hereonto afixed today,.......................</p>

  <p class="signature-label" style="left:287px; top:708px">President of the College</p>
  <p class="signature-label" style="left:715px; top:708px">Dean of the College</p>
</main>
</body>
</html>
```